Bellhaven Select Business Card Design Project

About the company: Here at Marigrove Essence, we focus on cosmetic products that based on essential oils and different kinds of plant essences. All of our raw materials are pure organic and specially selected from local producers in Australia.

I'm here to look for a unique business card design, to replace the current one later on, so I don't have many requirements. Why I wanna restrict designers' creativity?

All I know is: 1. do not make it too complicated, straight forward, simple and pure. 2. this design may be used for other purposes (i.e. logo and slogan on the front, Brand Story and contact details at the back). Therefor, I'd like to have the design for 3 layouts, one only have logo, slogan, contact detials, one for the brand story, the other one for the personal business card with staff's mob etc...

A vector graphic is required, i.e. eps, ai, easy for me to resize.

Round Corner.

Thanks
Updates

Plz add "Hand made in Australia" in the design, cheers.

Target Market(s)

Women aged yr 20-50

Industry/Entity Type

Business

Requirements
Must have
• Logo: please see attacment (eps, ai)

Slogan: Dew Touched Delight

Website:www.marigroveessence-demo.com.au

Address: temporary not available

Phone: temporary not available

"Hand made in Australia"

Nice to have
• Prefer round corner

```html
<!DOCTYPE html>
<html lang="en">
<head>
<meta charset="utf-8">
<title>Marigrove Essence – Business Card</title>
<link rel="stylesheet" href="https://fonts.googleapis.com/css2?family=EB+Garamond:ital,wght@0,400;0,500;1,400&display=swap">
<style>
  :root {
    --page-bg: #ffffff;
    --card-white: #ffffff;
    --band-deep: #b0384f;
    --band-rose: #cd4373;
    --band-mid: #d6637e;
    --band-soft: #e6b6c2;
    --brand-pink: #c6466f;
    --slogan-pink: #d4497a;
    --text-light: #ffffff;
    --rose-light: #f3c4d2;
    --rose-deep: #d56a8c;
  }
  * { box-sizing: border-box; margin: 0; padding: 0; }
  html, body {
    width: 1200px;
    height: 791px;
    overflow: hidden;
    background: var(--page-bg);
  }
  .canvas {
    position: relative;
    width: 1200px;
    height: 791px;
  }
  .card {
    position: absolute;
    left: 41px;
    top: 41px;
    width: 1119px;
    height: 708px;
    border-radius: 38px;
    overflow: hidden;
    background: linear-gradient(90deg, var(--band-deep) 0%, var(--band-rose) 28%, var(--band-mid) 55%, var(--band-soft) 100%);
    box-shadow: 0 4px 14px rgba(0, 0, 0, 0.28);
    font-family: "EB Garamond", Georgia, serif;
  }
  .card__top {
    position: absolute;
    left: 0;
    top: 0;
    width: 100%;
    height: 410px;
    background: var(--card-white);
    border-radius: 0 0 30px 30px;
  }
  .brand-name {
    position: absolute;
    left: 0;
    top: 185px;
    width: 100%;
    text-align: center;
    font-size: 64px;
    font-weight: 400;
    color: var(--brand-pink);
    letter-spacing: 2px;
  }
  .slogan {
    position: absolute;
    left: 141px;
    top: 338px;
    font-size: 21px;
    font-style: italic;
    color: var(--slogan-pink);
  }
  .rose-art {
    position: absolute;
    left: 397px;
    top: 308px;
    width: 160px;
    height: 152px;
    border-radius: 50%;
    background: radial-gradient(circle at 50% 45%, var(--rose-light) 0%, var(--rose-deep) 100%);
  }
  .contact {
    position: absolute;
    left: 64px;
    top: 485px;
    color: var(--text-light);
  }
  .contact__name {
    font-size: 29px;
    line-height: 1;
    margin-bottom: 32px;
  }
  .contact__line {
    font-size: 20px;
    line-height: 32px;
  }
  .origin-note {
    position: absolute;
    left: 660px;
    top: 622px;
    font-size: 20px;
    color: var(--text-light);
  }
</style>
</head>
<body>
  <main class="canvas">
    <article class="card">
      <section class="card__top">
        <div class="brand-name">Marigrove Essence</div>
        <p class="slogan">Dew Touched Delight</p>
      </section>
      <div class="rose-art" role="img" aria-label="Illustration of a pink rose blossom"></div>
      <section class="contact">
        <p class="contact__name">Name Surname</p>
        <p class="contact__line">Address: temporary not available</p>
        <p class="contact__line">Phone: temporary not available</p>
        <p class="contact__line">www.marigroveessence-demo.com.au</p>
      </section>
      <p class="origin-note">“Hand made in Australia”</p>
    </article>
  </main>
</body>
</html>
```